Design some Business Cards for eyelash / hair extensions

100% Guaranteed contest, check my history, perfect 5 star rating, I *always* select a winner and pay, even if we end up not using the winning design!!

Standard US size business cards, full color front and back.

You can see the information on the company and style here : [url removed, login to view]

Logo is attached.

Current card is attached - you can use the information on the card for your designs.

NOTES:

1) If we see something we like we will close the project early so get your work in quick!
2) Before selecting the winner, we sort by date to ensure you have not stolen your concept from someone else (no cheating!).
3) Final hand off design to be in adobe illustrator format - no exceptions!

Good luck!

```html
<!DOCTYPE html>
<html lang="en">
<head>
<meta charset="utf-8">
<title>Brows &amp; Braids – Business Card</title>
<link rel="stylesheet" href="https://fonts.googleapis.com/css2?family=Cormorant+Garamond:wght@500&family=Arimo:wght@400&display=swap">
<style>
  :root {
    --page: #e9e8ec;
    --paper: #ffffff;
    --sage: #a3ad86;
    --sage-light: #b2bb96;
    --sage-dark: #939d77;
    --ink: #5b5b57;
    --ink-dark: #4f514b;
    --white: #ffffff;
  }
  * { box-sizing: border-box; margin: 0; padding: 0; }
  html, body {
    width: 1200px;
    height: 1020px;
    overflow: hidden;
    background: var(--page);
  }
  .sheet {
    position: relative;
    width: 1200px;
    height: 1020px;
  }
  .card {
    position: absolute;
    left: 180px;
    width: 840px;
    height: 480px;
    overflow: hidden;
    box-shadow: 0 3px 10px rgba(0,0,0,0.18);
  }
  .card--front { top: 20px; background: var(--paper); }
  .card--back {
    top: 520px;
    background: linear-gradient(135deg, var(--sage-light) 0%, var(--sage) 55%, var(--sage-dark) 100%);
  }

  .brand {
    position: absolute;
    font-family: "Cormorant Garamond", Georgia, serif;
    font-weight: 500;
    letter-spacing: 0.5px;
    white-space: nowrap;
  }
  .card--front .brand {
    left: 0;
    right: 0;
    top: 100px;
    text-align: center;
    font-size: 70px;
    line-height: 1;
    color: var(--ink);
  }
  .card--back .brand {
    right: 80px;
    bottom: 80px;
    font-size: 48px;
    line-height: 1;
    color: var(--white);
    display: flex;
    align-items: center;
    gap: 16px;
  }
  .brand-dot {
    width: 14px;
    height: 14px;
    border-radius: 50%;
    background: var(--white);
  }

  .info-band {
    position: absolute;
    left: 0;
    right: 0;
    bottom: 0;
    height: 196px;
    background: var(--sage);
  }
  .flourish-front {
    position: absolute;
    right: 40px;
    bottom: 28px;
    width: 200px;
    height: 146px;
    border-radius: 20px;
    background: linear-gradient(160deg, #7a7e70 0%, #6a6d62 100%);
    opacity: 0.75;
  }
  .flourish-back {
    position: absolute;
    left: 110px;
    top: 70px;
    width: 300px;
    height: 340px;
    border-radius: 24px;
    background: rgba(255,255,255,0.07);
  }

  .contact {
    position: absolute;
    left: 40px;
    bottom: 36px;
    color: var(--white);
    font-family: "Arimo", Arial, sans-serif;
  }
  .contact-name {
    font-size: 24px;
    margin-bottom: 22px;
    white-space: nowrap;
  }
  .contact-name .divider {
    opacity: 0.7;
    margin: 0 8px;
  }
  .contact-role { font-size: 17px; }
  .contact-line {
    display: flex;
    align-items: center;
    gap: 12px;
    font-size: 17px;
    line-height: 26px;
  }
  .contact-line svg { width: 18px; height: 18px; flex: none; }
</style>
</head>
<body>
<main class="sheet">
  <section class="card card--front" aria-label="Card front">
    <div class="info-band"></div>
    <div class="flourish-front" role="img" aria-label="Decorative swirl flourish"></div>
    <div class="brand">Brows &amp; Braids</div>
    <div class="contact">
      <p class="contact-name">Dana Whitfield<span class="divider">|</span><span class="contact-role">Owner, Lash Stylist &amp; Aesthetician</span></p>
      <p class="contact-line">
        <svg viewBox="0 0 18 18" aria-hidden="true"><rect width="18" height="18" rx="3" fill="#5b5b57"/><path d="M5 4.5h2.4l1 2.6-1.3 1a6 6 0 0 0 2.8 2.8l1-1.3 2.6 1V13a1 1 0 0 1-1 1A9 9 0 0 1 4 5.5a1 1 0 0 1 1-1z" fill="#fff"/></svg>
        555.214.7730
      </p>
      <p class="contact-line">
        <svg viewBox="0 0 18 18" aria-hidden="true"><rect width="18" height="18" rx="3" fill="#5b5b57"/><circle cx="9" cy="9" r="5" fill="none" stroke="#fff" stroke-width="1.2"/><path d="M4 9h10M9 4c-2.2 2.8-2.2 7.2 0 10M9 4c2.2 2.8 2.2 7.2 0 10" fill="none" stroke="#fff" stroke-width="1"/></svg>
        www.browsbraids.com
      </p>
    </div>
  </section>

  <section class="card card--back" aria-label="Card back">
    <div class="flourish-back" role="img" aria-label="Faint decorative swirl pattern"></div>
    <div class="brand"><span class="brand-dot"></span>Brows &amp; Braids</div>
  </section>
</main>
</body>
</html>
```